Kvtrpa@mailbox.test

I am making this a landing page and I want to really grab the person and get them to call. So, I want some up front language at the top language about why they should contact me right away. The person looking is in a tough spot, they woe a lot of debt, they do not want to file a bankruptcy for moral or personal reasons, I want them to know that bankruptcy is a legal process that can help them and that they should not fear checking out their options. I will give them all of the information and if they want to go further fine, if not, they will have a lot more information about their situation and options

The language at the top, I want to be

Thanks for visiting us. You came here because you are having debt problems and you want solutions. Yes, we want your business. But, we don't want it if it is not right for you. We have been at this a long time and assisted thousands of Hawaii people and families with their debt problems. Many of those people were referred by former clients, but, our biggest referral source is people who did not file a bankruptcy. The reason is simple- our absolutely free and confidential consultation will help you get a handle on your whole situation. We will discuss your assets, your debts, your income and expenses and get a complete picture. It is only with this complete global picture of your particular situation that you can know your options, all of them, and then you can decide what is right for you. You are the driver. Call us at 472-3000 (from all islands) and let us help you today!

The color should be calming without being wimpy.

i want the top to be simple and a call to action giving people the sense that we know what we are doing and that they can call us for truly no obligation and we can help them diagnose their money issues and I can give them their options and they can do whatever they wish with them.

Target Market(s)

Hawaii people between ages of 28-70 who have credit card, loan or mortgage problems and need a way to get out of their debt

Industry/Entity Type

Legal

Requirements
Must have
• Must incorporate the items at qalmeridge.com. May be helpful to look at sunwardledger.com for example of the "clean clear" landing I would like to "grab" the customer's attention and get them to call me, phone is better than email. So must have contact us too.

```html
<!DOCTYPE html>
<html lang="en">
<head>
<meta charset="utf-8">
<title>Warren T. Halvorsen – Hawaii Bankruptcy Attorney</title>
<link href="https://fonts.googleapis.com/css2?family=Arimo:wght@400;700&family=Tinos:wght@400;700&display=swap" rel="stylesheet">
<style>
:root{
  --night:#17202b;
  --night-deep:#0f151d;
  --city-a:#3b4a58;
  --city-glow:#8a6a3a;
  --lemon:#e3e11f;
  --lime:#6aa61a;
  --paper:#ffffff;
  --mist:#eef0f2;
  --ink:#222;
  --sand:#f2e6cf;
  --sand-field:#fbf5e8;
}
*{box-sizing:border-box;margin:0;padding:0}
html,body{width:1200px;height:937px;overflow:hidden}
body{position:relative;background:var(--mist);font-family:Arimo,Arial,sans-serif;color:var(--ink)}
.abs{position:absolute}

.hero{left:0;top:0;width:1200px;height:410px;background:linear-gradient(180deg,var(--night-deep) 0,var(--city-a) 45%,var(--city-glow) 80%,#2b2a26 100%)}
.top-strip{left:0;top:0;width:1200px;height:46px;background:var(--night-deep);opacity:.85}
.top-rule{left:0;top:44px;width:1200px;height:4px;background:var(--lemon)}
.nav{left:520px;top:13px;display:flex;gap:10px;list-style:none}
.nav li{font-size:11px;color:#fff;padding:5px 9px}
.nav li.active{background:var(--lime)}

.brand{left:286px;top:40px;display:flex;align-items:center;gap:8px;font-size:17px;font-weight:700;color:#fff}
.brand i{display:block;width:14px;height:14px;background:var(--lemon)}

.like{left:754px;top:78px;display:flex;align-items:center;gap:6px;font-size:7px;color:#fff}
.like span.btn{background:#eceef3;color:#333;border:1px solid #999;padding:1px 4px;font-size:8px}

.banner{left:284px;top:103px;width:630px;height:60px;background:var(--lemon)}
.banner h1{position:absolute;left:16px;top:13px;font-size:16px;line-height:18px;font-weight:700;color:#111}
.banner .call{position:absolute;right:20px;top:18px;font-size:21px;font-weight:700;color:#111}
.spokes{left:600px;top:60px;width:96px;height:104px;background:linear-gradient(180deg,#3a3a3a,#111)}

.about-panel{left:292px;top:164px;width:622px;height:244px;background:rgba(15,20,28,.78)}
.about-head{left:310px;top:174px;color:#fff}
.about-head small{display:block;font-size:12px}
.about-head strong{display:block;font-size:21px;font-weight:700}
.about-copy{left:310px;top:216px;width:258px;font-size:9.2px;line-height:11.6px;color:#fff}
.promo{left:578px;top:182px;width:314px;height:208px;background:#fff;padding:4px}
.promo-photo{width:100%;height:100%;background:linear-gradient(160deg,#9fb2c0,#d6dde2 55%,#6f7f8c);position:relative}
.promo-quote{position:absolute;right:14px;top:30px;font-family:Tinos,Georgia,serif;font-size:13px;line-height:15px;color:#111}
.promo-foot{position:absolute;left:0;bottom:0;width:100%;height:40px;background:rgba(0,0,0,.55);color:#fff;font-family:Tinos,Georgia,serif;font-size:11.5px;line-height:14px;padding:6px 18px}

.green-band{left:0;top:410px;width:1200px;height:34px;background:linear-gradient(180deg,#8cc63e,var(--lime))}
.dark-band{left:0;top:444px;width:1200px;height:16px;background:var(--night)}

.main-card{left:289px;top:422px;width:417px;height:424px;background:var(--paper);border:1px solid #ddd}
.block-title{position:absolute;height:24px;background:linear-gradient(180deg,#333,#111);color:#fff;font-size:15px;line-height:24px;padding-left:8px}
.links{position:absolute;list-style:none;font-size:7.6px;line-height:9.2px;color:#222}
.links li{padding-left:10px;position:relative;margin-bottom:2px}
.links li::before{content:"›";position:absolute;left:1px;color:#666}

.video{left:304px;top:667px;width:178px;height:166px;background:linear-gradient(160deg,#6b5a4c,#a58a6e 60%,#3b2f27)}
.video-bar{position:absolute;left:0;bottom:0;width:100%;height:16px;background:#222}
.video-play{position:absolute;left:74px;top:68px;width:30px;height:20px;background:rgba(0,0,0,.75);border-radius:4px}
.testi-title{left:498px;top:664px;font-size:12px;font-weight:700}
.testi-rule{left:498px;top:681px;width:194px;height:1px;background:#ccc}
.testi{left:500px;top:690px;width:192px;font-size:7.4px;line-height:9.2px;color:#333}
.testi p{margin-bottom:8px}
.more-btn{left:500px;top:817px;width:115px;height:16px;background:var(--lime);color:#fff;font-size:7px;font-weight:700;text-align:center;line-height:16px}

.consult{left:719px;top:422px;width:190px;height:218px;background:var(--sand);border:1px solid #d9c9a6}
.consult h2{height:30px;background:linear-gradient(180deg,#333,#111);color:#fff;font-weight:400;font-size:16px;line-height:30px;padding-left:17px}
.consult .intro{font-size:7.8px;line-height:10px;margin:10px 10px 6px;color:#333}
.field{display:flex;margin:0 10px 6px;font-size:7.2px;line-height:8.4px}
.field label{width:54px;padding-top:3px}
.field span{flex:1;height:21px;background:var(--sand-field);border:1px solid #e2d3b5}
.field.msg span{height:40px}
.consult .foot{display:flex;justify-content:space-between;align-items:center;margin:4px 10px 0}
.consult .foot a{font-size:7px;color:#111;text-decoration:underline}
.consult .foot b{background:var(--lime);color:#fff;font-size:11px;padding:4px 16px}

.family{left:719px;top:652px;width:190px;height:62px;background:linear-gradient(90deg,#7a6a4e,#b89f7a 50%,#5f7648)}
.since{left:720px;top:717px;font-size:8.5px}
.contact-title{left:719px;top:738px;font-size:11.5px;font-weight:700}
.map{left:719px;top:757px;width:77px;height:62px;background:linear-gradient(135deg,#e8e6dc,#d3d8c7)}
.address{left:814px;top:756px;font-size:7.4px;line-height:9.6px;color:#333}

.footer-rule{left:0;top:856px;width:1200px;height:3px;background:var(--lemon)}
.footer{left:0;top:859px;width:1200px;height:78px;background:var(--night)}
.badge{left:292px;top:858px;width:98px;height:68px;background:#fff;border:1px solid #bbb}
.badge i{position:absolute;left:6px;top:8px;width:30px;height:48px;background:#6f8fae}
.badge p{position:absolute;left:41px;top:13px;font-size:6.5px;line-height:8px;color:#333}
.follow{left:686px;top:875px;font-size:10.5px;color:#fff;display:flex;align-items:center;gap:4px}
.follow i{display:inline-block;width:10px;height:10px;background:#5a6a7c}
.flinks{left:686px;top:891px;font-size:6.7px;line-height:9.6px;color:#fff}
.flinks u{text-decoration:underline}
</style>
</head>
<body>

<div class="abs hero" role="img" aria-label="Night skyline of downtown Honolulu with lit streets"></div>
<div class="abs top-strip"></div>
<div class="abs top-rule"></div>
<ul class="abs nav">
  <li class="active">Home</li><li>About Us</li><li>Chapter 7</li><li>Chapter 13</li><li>Testimonials</li><li>Blog</li><li>Contact Us</li>
</ul>

<div class="abs brand"><i></i>Warren T. Halvorsen</div>

<div class="abs like"><span class="btn">Like</span>Be the first of your friends to like this</div>

<div class="abs banner">
  <h1>HAWAII BANKRUPTCY ATTORNEY<br>AND DEBT SOLUTIONS</h1>
  <div class="call">Call: 808-472-3000</div>
</div>
<div class="abs spokes" role="img" aria-label="Welcoming staff member in a dark suit"></div>

<div class="abs about-panel"></div>
<div class="abs about-head"><small>About</small><strong>Warren T. Halvorsen</strong></div>
<p class="abs about-copy">Thanks for visiting us. You came here because you are having debt problems and you want solutions. Yes, we want your business. But, we don't want it if it is not right for you. We have been at this a long time and assisted thousands of Hawaii people and families with their debt problems. Many of those people were referred by former clients, but, our biggest referral source is people who did not file a bankruptcy. The reason is simple- our absolutely free and confidential consultation will help you get a handle on your whole situation. We will discuss your assets, your debts, your income and expenses and get a complete picture. It is only with this complete global picture of your particular situation that you can know your options, all of them, and then you can decide what is right for you. You are the driver. Call us at 472-3000 (from all islands) and let us help you today!</p>

<div class="abs promo">
  <div class="promo-photo" role="img" aria-label="Relieved young professional in shirt and tie in the city">
    <div class="promo-quote">No Collector calls,<br>no harassment, no debts<br>- Feels Great!</div>
    <div class="promo-foot">Get The Feeling!<br>Feel what its like to be debt free!</div>
  </div>
</div>

<div class="abs green-band"></div>
<div class="abs dark-band"></div>

<div class="abs main-card"></div>
<div class="block-title" style="left:304px;top:434px;width:174px">Recent Articles</div>
<ul class="links" style="left:302px;top:462px;width:180px">
  <li>What Is Lien Stripping in a Chapter 13 Hawaii Bankruptcy?</li>
  <li>What Is A Co-Debtor Stay in a Chapter 13 Hawaii Bankruptcy?</li>
  <li>What is Chapter 13 Bankruptcy in Hawaii?</li>
  <li>What is Chapter 7 Bankruptcy in Hawaii?</li>
  <li>What is a Hawaii bankruptcy estate?</li>
</ul>
<div class="block-title" style="left:514px;top:434px;width:176px">Resources</div>
<ul class="links" style="left:514px;top:462px;width:180px">
  <li>Why shouldn't I consolidate my debt?</li>
  <li>What happens to my tax return if I file bankruptcy?</li>
  <li>What can be done if your car is worth less than what you owe.</li>
  <li>What if my house is worth less than I owe?</li>
  <li>Co Debtor Stay</li>
</ul>
<div class="block-title" style="left:304px;top:548px;width:174px">Recent Videos</div>
<ul class="links" style="left:302px;top:576px;width:180px">
  <li>Why a Chapter 13 needs to be Feasible.</li>
  <li>What happens to my tax return if I file bankruptcy?</li>
  <li>What can be done if your car is worth less than what you owe.</li>
  <li>What if my house is worth less than I owe?</li>
  <li>Co Debtor Stay</li>
</ul>
<div class="block-title" style="left:514px;top:548px;width:176px">Categories</div>
<ul class="links" style="left:514px;top:576px;width:86px">
  <li>Articles</li><li>Bankruptcy</li><li>Bankruptcy Hawaii</li><li>Bankruptcy Honolulu</li><li>Bankruptcy oahu</li><li>Blog</li>
</ul>
<ul class="links" style="left:606px;top:576px;width:86px">
  <li>Blogroll</li><li>CARE</li><li>Chapter 13</li><li>Chapter 13 Bankruptcy Hawaii</li>
</ul>

<div class="abs video" role="img" aria-label="Video still of the attorney speaking in his office">
  <div class="video-play"><svg width="30" height="20" viewBox="0 0 30 20"><path d="M12 5 L20 10 L12 15 Z" fill="#fff"/></svg></div>
  <div class="video-bar"><svg width="178" height="16" viewBox="0 0 178 16"><path d="M6 4 L12 8 L6 12 Z" fill="#ccc"/><rect x="20" y="4" width="4" height="8" fill="#ccc"/><text x="60" y="11" font-size="7" fill="#ccc" font-family="Arimo,Arial,sans-serif">0:00 / 0:00</text></svg></div>
</div>
<div class="abs testi-title">Client Testimonials</div>
<div class="abs testi-rule"></div>
<div class="abs testi">
  <p>"Thanks for the good news about R's plan..... I also want to say thank you for always treating my mother with consideration. Your mindfulness, acuity, and helpfulness will always be remembered..."--HT</p>
  <p>"Thank you for guiding me during this difficult period of my life. I was unfamiliar with bankruptcy and my experience with you was nothing but positive..."--RK</p>
  <p>"I never thought in a million years I would have to even consider bankruptcy... Mr. Halvorsen made it as painless as possible and I would highly recommend him to anyone. Thanks Warren!"--TS</p>
</div>
<div class="abs more-btn">Click here for more testimonials...</div>

<div class="abs consult">
  <h2>Free Consultation</h2>
  <p class="intro">Fill out the form below for a free no obligation consultation, or <b>Call: 808-472-3000</b></p>
  <div class="field"><label>Your Name (required)</label><span></span></div>
  <div class="field"><label>Your Email (required)</label><span></span></div>
  <div class="field"><label>Your Phone (required)</label><span></span></div>
  <div class="field msg"><label>Your Name Message</label><span></span></div>
  <div class="foot"><a>Read Our Privacy Statement</a><b>Submit</b></div>
</div>

<div class="abs family" role="img" aria-label="Smiling Hawaii family outside their home"></div>
<div class="abs since">Serving Hawaii Since 1995</div>
<div class="abs contact-title">Contact Info</div>
<div class="abs map" role="img" aria-label="Small street map of the downtown Honolulu office"></div>
<div class="abs address">Warren T. Halvorsen,<br>Attorney-at-Law<br>2240 Kapena St. Suite 1410<br>Honolulu, HI 96815<br>808-472-3000<br>info@qalmeridge.com<br><br>View larger map and<br>directions</div>

<div class="abs footer-rule"></div>
<div class="abs footer"></div>
<div class="abs badge"><i></i><p>Pacific<br>Alliance of<br>Consumer<br>Debt<br>Counsel</p></div>
<div class="abs follow">Follow Us On: <i></i><i></i><i></i></div>
<div class="abs flinks">Home -- About Us -- Chapter 7 -- Chapter 13 -- Blog -- Contact Us<br><u>Site Map</u>, <u>Privacy Statement</u>, <u>Terms of Service</u><br>© 2011 Warren T. Halvorsen. All rights reserved.</div>

</body>
</html>
```